Ninety Truths Earned Across Four Decades of Advisory Work

I need the design for my book cover, plus the spine and the back cover. I need this for both a hard cover book and an ebook

Target Market(s)

Any person in business with managerial responsibility

Industry/Entity Type

Consulting

Font styles to use
Serif

Requirements
Must have
• Must look very professional. No script/cursive is to be used. The cover should be clean, not cluttered.so the title really stands out well
Nice to have
• A professional image to reinforce the title
Should not have
• Script, cartoons or anything that does not look professional

```html
<!DOCTYPE html>
<html lang="en">
<head>
<meta charset="utf-8">
<title>Ninety Truths Earned Across Four Decades of Advisory Work – Cover</title>
<link rel="stylesheet" href="https://fonts.googleapis.com/css2?family=Antonio:wght@700&family=Archivo:wght@600&display=swap">
<style>
  :root {
    --backdrop: #2a2a2b;
    --cover-paper: #ffffff;
    --title-navy: #1b2340;
    --subtitle-ink: #111114;
    --art-pale: #e8edf7;
    --art-mid: #b9c4e6;
    --art-deep: #8f9fd6;
  }
  html, body {
    margin: 0;
    padding: 0;
    width: 687px;
    height: 1200px;
    overflow: hidden;
    background: var(--backdrop);
  }
  .canvas {
    position: relative;
    width: 687px;
    height: 1200px;
  }
  .book-cover {
    position: absolute;
    left: 23px;
    top: 120px;
    width: 640px;
    height: 960px;
    background: var(--cover-paper);
    box-shadow: 0 18px 40px rgba(0,0,0,0.45);
    text-align: center;
  }
  .cover-title {
    margin: 0;
    padding: 64px 56px 0;
  }
  .title-major {
    display: block;
    font-family: "Antonio", "Oswald", sans-serif;
    font-weight: 700;
    font-size: 82px;
    line-height: 1;
    letter-spacing: -0.5px;
    color: var(--title-navy);
    text-transform: uppercase;
  }
  .title-minor {
    display: block;
    font-family: "Archivo", "Helvetica Neue", sans-serif;
    font-weight: 600;
    font-size: 36px;
    line-height: 1.1;
    color: var(--subtitle-ink);
    text-transform: uppercase;
    margin: 14px 0 16px;
  }
  .cover-art {
    position: absolute;
    left: 110px;
    top: 450px;
    width: 420px;
    height: 470px;
    border-radius: 210px 210px 12px 12px;
    background: radial-gradient(circle at 50% 32%, var(--art-deep) 0%, var(--art-mid) 30%, var(--art-pale) 58%, var(--cover-paper) 100%);
  }
</style>
</head>
<body>
  <main class="canvas">
    <article class="book-cover">
      <h1 class="cover-title">
        <span class="title-major">Ninety Truths</span>
        <span class="title-minor">Earned Across</span>
        <span class="title-major">Four Decades of</span>
        <span class="title-minor">Advisory Work</span>
      </h1>
      <div class="cover-art" role="img" aria-label="Illustration of two business consultants in dark suits standing before a pale blue ring chart and a seated meeting audience"></div>
    </article>
  </main>
</body>
</html>
```